Voranel.com Personal Trainer/Fitness Website

I want a website to market my personal training/Outdoor Bootcamp Class services, as well as to ditribute nutrivexa. I need a logo as well I included an address for the Harbor Gales 1975 logo. I'd like Voranel in place of Harbor Gales, and in Black and white, just different enough so I can't get sued by the PLX.
https://www.pictofind.example/imgres?imgurl=http%3A%2F%2Fwww.dorian-halverstock.example%2Fwp-content%2Fuploads%2F2014%2F01%2Fgales_mark4.jpg&imgrefurl=http%3A%2F%2Fwww.dorian-halverstock.example%2Fplx-emblem-reworks-tulsa-harbor-bolts%2F&docid=_qweRT8uPLmnBx&tbnid=k3tyA7XbNqwePZ%3A&w=600&h=450&client=ms-android-carrierx&bih=512&biw=360&ved=0ahUKEwiQazxcv7LMAhUTwGMKHRPMBWMQMwg6KBQwFA&iact=mrc&uact=8.
It should be about 5 pages 1. home 2. about 3. Services 4. Blog/Videos and programs 5. Contact.
http://www.tobenwelfitness.example.uk/ is a website I like the style of.

Target Market(s)

Seattle area

Industry/Entity Type

Fitness

Coding

Coded - Design and coding required

Number of Pages Required

4 page

Font styles to use
Serif
Sans Serif

Requirements
Must have
• A minimal look
Nice to have
• A logo similar to the 1975 Harbor Galewinds Logo, with a Small Dorn Velask ripping his shirt open(with a picture of the logo on his shirt, picture within picture) to turn into Skyvaler in the center. Skyline is black, Background and small figure white(with black logo on shirt)

```html
<!DOCTYPE html>
<html lang="en">
<head>
<meta charset="utf-8">
<title>Voranel — Personal Training &amp; Outdoor Bootcamp</title>
<link href="https://fonts.googleapis.com/css2?family=Exo+2:wght@500;600;700;800&family=Open+Sans:wght@400;600;700&display=swap" rel="stylesheet">
<style>
:root{
  --ink:#000;
  --white:#fff;
  --text:#333;
  --muted:#cfcfcf;
  --band:#262626;
  --panel:#3a3a3a;
  --panel-dark:#2b2b2b;
  --button:#3f3f3f;
  --accent:#9ccc5a;
  --footer:#1b1b1b;
  --line:#555;
  --fb:#3b5998;--tw:#1da1f2;--yt:#e52d27;--gp:#dd4b39;
}
*{box-sizing:border-box;margin:0;padding:0}
html,body{width:1200px;height:3285px;overflow:hidden}
body{position:relative;background:var(--white);font-family:"Open Sans",Arial,sans-serif;color:var(--text)}
.abs{position:absolute}
.head{font-family:"Exo 2","Trebuchet MS",sans-serif}
.center{text-align:center}
section,header,nav,footer{position:absolute;left:0;width:1200px}

/* header */
.site-header{top:0;height:136px;background:var(--white)}
.brand-mark{left:79px;top:40px;width:54px;height:54px;border-radius:50%;background:var(--ink)}
.brand-name{left:146px;top:48px;font:800 32px/1 "Exo 2",sans-serif;color:var(--ink);letter-spacing:1px}
.member-btn{left:904px;top:22px;width:215px;height:44px;background:var(--ink);border-radius:4px;color:var(--white);font:700 14px/44px "Open Sans",sans-serif;text-align:center;letter-spacing:.3px}
.member-btn svg{vertical-align:-4px;margin-right:8px}
.phone-icon{left:755px;top:86px;width:28px;height:28px;border-radius:50%;background:#bdbdbd}
.phone-num{left:792px;top:88px;font:700 17px/24px "Open Sans",sans-serif;color:var(--ink)}
.social{top:84px;width:30px;height:30px;border-radius:50%}

/* nav */
.main-nav{top:136px;height:44px;background:var(--ink);display:flex;padding-left:83px}
.main-nav a{display:block;height:44px;line-height:44px;text-align:center;color:var(--white);font:700 14px/44px "Open Sans",sans-serif;text-decoration:none;border-right:1px solid #333}
.main-nav a.active{background:#444}

/* hero */
.hero{top:180px;height:611px;background:linear-gradient(180deg,#6f8d5a 0%,#8aa36c 35%,#4f6a3f 70%,#2f3a2c 100%)}
.hero-title-1{top:262px;width:1200px;font:700 36px/1 "Exo 2",sans-serif;color:var(--white)}
.hero-title-2{top:316px;width:1200px;font:800 45px/1 "Exo 2",sans-serif;color:var(--white)}
.hero-btn{left:493px;top:392px;width:192px;height:48px;background:var(--white);border-radius:3px;font:700 16px/48px "Open Sans",sans-serif;color:var(--ink);text-align:center}
.dot{top:521px;width:12px;height:12px;border-radius:50%;background:rgba(255,255,255,.55)}
.dot.on{background:var(--white)}

/* promo */
.promo{top:791px;height:177px;background:linear-gradient(90deg,#2d2d2d,#1f1f1f 50%,#2a2a2a)}
.promo-h{top:38px;width:330px;font:500 23px/28px "Exo 2",sans-serif;color:var(--white);text-align:center}
.promo-btn{top:89px;height:44px;background:var(--button);color:var(--white);font:700 17px/44px "Exo 2",sans-serif;text-align:center;letter-spacing:.5px}
.offer{left:410px;top:-11px;width:383px;height:195px;background:var(--panel);z-index:2;box-shadow:0 0 12px rgba(0,0,0,.5)}
.offer-1{top:22px;width:383px;font:700 30px/34px "Exo 2",sans-serif;color:var(--white)}
.offer-2{top:74px;width:383px;font:800 35px/38px "Exo 2",sans-serif;color:var(--accent)}
.offer-tab{left:30px;top:140px;width:323px;height:55px;background:var(--panel-dark);border-radius:40px 40px 0 0/28px 28px 0 0;font:700 23px/60px "Exo 2",sans-serif;color:var(--white);text-align:center}

/* services */
.services{top:968px;height:526px;background:radial-gradient(ellipse at 50% 40%,#555 0%,#3e3e3e 60%,#333 100%)}
.sec-title{width:1200px;font:700 32px/1 "Exo 2",sans-serif;color:var(--white)}
.rule{height:1px;background:#9a9a9a}
.lead{left:219px;top:148px;width:760px;font:400 14px/24px "Open Sans",sans-serif;color:var(--white)}
.svc{top:212px;width:250px;text-align:center}
.svc-icon{margin:0 auto;width:118px;height:118px;border-radius:50%;background:var(--ink);border:4px solid var(--white);display:flex;align-items:center;justify-content:center}
.svc-name{margin-top:24px;font:600 19px/24px "Exo 2",sans-serif;color:var(--white)}
.svc-text{margin-top:10px;font:400 12.5px/19px "Open Sans",sans-serif;color:var(--white)}
.plus{margin:26px auto 0;width:24px;height:24px;background:var(--white);color:var(--ink);font:700 20px/24px Arial,sans-serif}

/* welcome */
.welcome{top:1494px;height:291px;background:var(--white)}
.welcome-title{top:34px;width:1200px;font:700 30px/32px "Exo 2",sans-serif;color:#222;letter-spacing:1px}
.welcome-title span.badge{display:inline-block;width:34px;height:24px;border:3px solid #222;border-radius:17px 17px 3px 3px;vertical-align:-2px;margin-right:14px}
.welcome-text{left:114px;top:121px;width:974px;font:400 15px/24px "Open Sans",sans-serif;color:#222}
.small-btn{background:var(--ink);color:var(--white);font:700 12px/26px "Open Sans",sans-serif;text-align:center}

/* amenities */
.amenities{top:1785px;height:412px;overflow:hidden}
.amen-photo-l{left:0;top:0;width:620px;height:412px;background:linear-gradient(120deg,#7d92a3 0%,#9aa28a 35%,#6d5a48 70%,#4a3c30 100%)}
.amen-photo-r{left:600px;top:0;width:600px;height:412px;background:linear-gradient(160deg,#d8d8d8 0%,#9a9a9a 45%,#5a5a5a 100%)}
.amen-t1{left:380px;top:64px;width:400px;font:700 30px/32px "Exo 2",sans-serif;color:var(--white)}
.amen-t2{left:380px;top:110px;width:400px;font:800 42px/44px "Exo 2",sans-serif;color:var(--white);letter-spacing:1px}
.amen-text{left:380px;top:186px;width:400px;font:400 16px/28.5px "Open Sans",sans-serif;color:var(--white)}
.amen-btn{left:486px;top:304px;width:162px;height:48px;background:var(--button);color:var(--white);font:700 17px/48px "Exo 2",sans-serif;text-align:center}

/* feature cards */
.card{top:2247px;width:324px;height:177px;background:linear-gradient(135deg,#6a6a6a,#4a4a4a 60%,#3c3c3c)}
.card-label{width:324px;font:700 24px/26px "Exo 2",sans-serif;color:var(--white);text-align:center}

/* events */
.events{top:2488px;height:289px;background:var(--ink)}
.events-photo{left:0;top:0;width:600px;height:289px;background:linear-gradient(110deg,#c9cfc6 0%,#9aa49a 40%,#6f776e 75%,#555 100%)}
.events-title{left:639px;top:42px;font:700 28px/44px "Exo 2",sans-serif;color:var(--white)}
.events-text{left:639px;top:140px;width:460px;font:400 13px/22px "Open Sans",sans-serif;color:var(--white)}
.events-btn{left:639px;top:204px;width:143px;height:43px;background:#333;border:1px solid #555;color:var(--white);font:700 14px/41px "Open Sans",sans-serif;text-align:center}

/* footer */
.site-footer{top:2777px;height:460px;background:linear-gradient(180deg,#2a2a2a 0%,var(--footer) 35%,#141414 100%)}
.news{left:81px;top:55px;width:740px;height:65px;border:1px solid var(--line);background:rgba(255,255,255,.03)}
.news-label{left:19px;top:20px;font:400 18px/24px "Open Sans",sans-serif;color:var(--white)}
.news-input{left:223px;top:15px;width:386px;height:33px;background:var(--white);font:400 12px/33px "Open Sans",sans-serif;color:#333;padding-left:8px}
.news-btn{left:609px;top:15px;width:120px;height:33px;background:var(--ink);color:var(--white);font:600 12px/33px "Open Sans",sans-serif;text-align:center}
.follow{left:843px;top:73px;font:600 18px/24px "Open Sans",sans-serif;color:var(--white)}
.ring{top:70px;width:30px;height:30px;border:2px solid #bbb;border-radius:50%}
.f-title{font:700 18px/24px "Exo 2",sans-serif;color:var(--white)}
.field{border:1px solid var(--line);font:400 12px/35px "Open Sans",sans-serif;color:#ddd;padding-left:10px}
.submit{background:#3a3a3a;color:var(--white);font:700 13px/37px "Open Sans",sans-serif;text-align:center}
.links{left:630px;top:224px;list-style:none}
.links li{font:400 14px/27px "Open Sans",sans-serif;color:#ddd}
.links li::before{content:"›";margin-right:10px;color:#aaa}
.links li.current{color:var(--white);font-weight:700}
.c-text{font:400 12.5px/22px "Open Sans",sans-serif;color:#ddd}
.vsep{width:1px;background:#3a3a3a}
.to-top{left:584px;top:3228px;width:32px;height:10px;background:#555;clip-path:polygon(20% 0,80% 0,100% 100%,0 100%)}
.copyright{top:3237px;height:48px;background:#2e2e2e;border-top:4px solid #555;font:400 12px/44px "Open Sans",sans-serif;color:var(--white);text-align:center}
</style>
</head>
<body>

<header class="site-header">
  <div class="abs brand-mark"></div>
  <div class="abs brand-name">VORANEL</div>
  <div class="abs member-btn"><svg width="16" height="16" viewBox="0 0 16 16"><circle cx="7" cy="5" r="3.5" fill="#fff"/><path d="M1 15c0-4 3-6 6-6s6 2 6 6z" fill="#fff"/></svg>BECOME A MEMBER</div>
  <div class="abs phone-icon"><svg width="28" height="28" viewBox="0 0 28 28"><path d="M10 8l3 3-2 2c1 2 3 4 5 5l2-2 3 3-2 3c-5 0-11-6-11-11z" fill="#fff"/></svg></div>
  <div class="abs phone-num">123-456-7890</div>
  <div class="abs social" style="left:957px;background:var(--fb)"></div>
  <div class="abs social" style="left:1000px;background:var(--tw)"></div>
  <div class="abs social" style="left:1043px;background:var(--yt)"></div>
  <div class="abs social" style="left:1086px;background:var(--gp)"></div>
</header>

<nav class="main-nav">
  <a class="active" style="width:97px">HOME</a>
  <a style="width:153px">ABOUT</a>
  <a style="width:171px">SERVICES</a>
  <a style="width:131px">BLOG</a>
  <a style="width:149px">VIDEOS</a>
  <a style="width:197px">PROGRAMS</a>
  <a style="width:138px;border-right:0">CONTACT</a>
</nav>

<section class="hero" role="img" aria-label="Group of smiling people stretching arms overhead during an outdoor workout in a sunny park">
  <div class="abs hero-title-1 center" style="top:82px">GET FIT AND HAVE FUN</div>
  <div class="abs hero-title-2 center" style="top:136px">THE WAY IT SHOULD BE</div>
  <div class="abs hero-btn" style="top:392px">GET STARTED</div>
  <div class="abs dot on" style="left:558px"></div>
  <div class="abs dot" style="left:588px"></div>
  <div class="abs dot" style="left:626px"></div>
</section>

<section class="promo">
  <div class="abs promo-h" style="left:76px">Get Access To All Facilites</div>
  <div class="abs promo-btn" style="left:129px;width:221px">SUBSCRIBE NOW</div>
  <div class="abs offer">
    <div class="abs offer-1 center">Signup For 6 Month</div>
    <div class="abs offer-2 center">Get 30% off</div>
    <div class="abs offer-tab">SIGN UP!</div>
  </div>
  <div class="abs promo-h" style="left:799px">Offer Free Consultation</div>
  <div class="abs promo-btn" style="left:839px;width:245px">GET CONSULTATION</div>
</section>

<section class="services">
  <div class="abs sec-title center" style="top:65px">OUR SERVICES</div>
  <div class="abs rule" style="left:383px;top:120px;width:646px"></div>
  <p class="abs lead center">Lorem ipsum dolor sit amet, consectetur adipiscing elit. Morbi quis ante sed massa consectetur feugiat id at tellus. Fusce tristique dictum tincidunt. Nam viverra euismod pretium</p>

  <div class="abs svc" style="left:59px">
    <div class="svc-icon"><svg width="60" height="60" viewBox="0 0 60 60"><rect x="8" y="24" width="8" height="12" fill="#fff"/><rect x="44" y="24" width="8" height="12" fill="#fff"/><rect x="16" y="20" width="5" height="20" fill="#fff"/><rect x="39" y="20" width="5" height="20" fill="#fff"/><rect x="21" y="28" width="18" height="4" fill="#fff"/></svg></div>
    <div class="svc-name">Personal Training</div>
    <div class="svc-text">Liorem ipsum dolor sit amet,<br>consecte adipiscing elit, sed diam</div>
    <div class="plus">+</div>
  </div>
  <div class="abs svc" style="left:344px">
    <div class="svc-icon"><svg width="60" height="60" viewBox="0 0 60 60"><circle cx="30" cy="33" r="17" fill="none" stroke="#fff" stroke-width="4"/><rect x="26" y="10" width="8" height="5" fill="#fff"/><path d="M30 33V22" stroke="#fff" stroke-width="4"/></svg></div>
    <div class="svc-name">Outdoor Bootcamp Classes</div>
    <div class="svc-text">Liorem ipsum dolor sit amet,<br>consecte adipiscing elit, sed diam</div>
    <div class="plus">+</div>
  </div>
  <div class="abs svc" style="left:633px">
    <div class="svc-icon"><svg width="60" height="60" viewBox="0 0 60 60"><path d="M18 50V10" stroke="#fff" stroke-width="4"/><path d="M20 12h24l-6 8 6 8H20z" fill="#fff"/></svg></div>
    <div class="svc-name">Outdoor Group Training</div>
    <div class="svc-text">Liorem ipsum dolor sit amet,<br>consecte adipiscing elit, sed diam</div>
    <div class="plus">+</div>
  </div>
  <div class="abs svc" style="left:889px">
    <div class="svc-icon"><svg width="60" height="60" viewBox="0 0 60 60"><rect x="10" y="14" width="40" height="26" rx="2" fill="none" stroke="#fff" stroke-width="4"/><rect x="26" y="40" width="8" height="6" fill="#fff"/><rect x="20" y="46" width="20" height="4" fill="#fff"/></svg></div>
    <div class="svc-name">Online Coaching</div>
    <div class="svc-text">Liorem ipsum dolor sit amet,<br>consecte adipiscing elit, sed diam</div>
    <div class="plus">+</div>
  </div>
</section>

<section class="welcome">
  <div class="abs welcome-title center"><span class="badge"></span>WELCOME TO VORANEL</div>
  <div class="abs rule" style="left:114px;top:89px;width:974px;background:#ddd"></div>
  <div class="abs rule" style="left:520px;top:88px;width:160px;height:2px;background:#444"></div>
  <p class="abs welcome-text center">Lorem ipsum dolor sit amet, consectetuer adipiscing elit, sed diam nonummy nibh euismod tincidunt ut laoreet dolore magna aliquam erat volutpat. Ut wisi enim ad minim veniam, quis nostrud exerci tation ullamcorper suscipit lobortis nisl ut aliquip ex ea commodo consequat. Duis autem vel eum iriure dolor in hendrerit in vulputate velit esse molestie consequat, vel illum dolore eu feugiat nulla facilisis.</p>
  <div class="abs small-btn" style="left:548px;top:215px;width:105px;height:26px">READ MORE</div>
</section>

<section class="amenities">
  <div class="abs amen-photo-l" role="img" aria-label="Outdoor bootcamp group doing push-ups on mats with mountains behind"></div>
  <div class="abs amen-photo-r" role="img" aria-label="Black and white row of treadmills in a gym"></div>
  <svg class="abs" style="left:0;top:0" width="1200" height="412"><polygon points="434,0 832,0 755,412 361,412" fill="#141414"/></svg>
  <svg class="abs" style="left:156px;top:158px" width="100" height="100"><circle cx="50" cy="50" r="47" fill="none" stroke="#fff" stroke-width="4"/><polygon points="40,30 72,50 40,70" fill="#fff"/></svg>
  <div class="abs amen-t1 center">STATE OF THE ART</div>
  <div class="abs amen-t2 center">AMENITIES</div>
  <p class="abs amen-text center">FEATURING THE BEST<br>EQUIPMENT, LOCKER ROOMS,<br>SMOOTHIE BAR &amp; MORE.</p>
  <div class="abs amen-btn">LEARN MORE</div>
</section>

<div class="abs card" style="left:81px" role="img" aria-label="Trainer consulting with a client at a desk">
  <svg class="abs" style="left:132px;top:40px" width="60" height="50"><rect x="4" y="4" width="34" height="22" rx="4" fill="#fff"/><polygon points="10,26 18,26 10,34" fill="#fff"/><rect x="24" y="18" width="32" height="20" rx="4" fill="none" stroke="#fff" stroke-width="3"/></svg>
  <div class="abs card-label" style="top:121px">Free Consultation</div>
</div>
<div class="abs card" style="left:438px" role="img" aria-label="Fresh fruit and healthy food">
  <svg class="abs" style="left:137px;top:36px" width="50" height="54"><path d="M25 14c-6-4-20-3-20 14 0 14 10 24 20 20 10 4 20-6 20-20 0-17-14-18-20-14z" fill="#fff"/><path d="M25 14c0-6 4-10 10-12" stroke="#fff" stroke-width="3" fill="none"/></svg>
  <div class="abs card-label" style="top:121px">Nutrition Guidance</div>
</div>
<div class="abs card" style="left:795px" role="img" aria-label="Personal trainer coaching a client in the gym">
  <svg class="abs" style="left:132px;top:28px" width="60" height="40"><rect x="6" y="12" width="8" height="16" fill="#fff"/><rect x="46" y="12" width="8" height="16" fill="#fff"/><rect x="14" y="18" width="32" height="4" fill="#fff"/></svg>
  <div class="abs card-label" style="top:100px">Get A<br>Personal Trainer</div>
</div>

<section class="events">
  <div class="abs events-photo" role="img" aria-label="Smiling group of women stretching together at a fitness event"></div>
  <div class="abs events-title">We Organize &amp; Participate<br>In Group Events</div>
  <p class="abs events-text">Lorem ipsum dolor sit amet, consectetuer adipiscing elit, sed diam nonummy nibh euismod tincidunt ut laoreet dolore magna aliquam erat volutpat.</p>
  <div class="abs events-btn">LEARN MORE</div>
</section>

<footer class="site-footer">
  <div class="abs news">
    <svg class="abs" style="left:14px;top:22px" width="22" height="20"><rect x="1" y="3" width="20" height="14" fill="none" stroke="#fff" stroke-width="2"/><path d="M1 3l10 8 10-8" stroke="#fff" stroke-width="2" fill="none"/></svg>
    <div class="abs news-label" style="left:44px">Newsletter Signup</div>
    <div class="abs news-input">Enter your email here</div>
    <div class="abs news-btn">SUBSCRIBE</div>
  </div>
  <div class="abs follow">Follow Us</div>
  <div class="abs ring" style="left:964px"></div>
  <div class="abs ring" style="left:997px"></div>
  <div class="abs ring" style="left:1030px"></div>
  <div class="abs ring" style="left:1063px"></div>

  <svg class="abs" style="left:81px;top:166px" width="24" height="24"><circle cx="12" cy="12" r="10" fill="none" stroke="#fff" stroke-width="2"/><text x="12" y="17" text-anchor="middle" fill="#fff" font-family="Arial,sans-serif" font-weight="700" font-size="14">?</text></svg>
  <div class="abs f-title" style="left:114px;top:164px;font-size:24px;line-height:28px">QUICK INQUIRY</div>
  <div class="abs field" style="left:81px;top:232px;width:226px;height:37px">Name</div>
  <div class="abs field" style="left:81px;top:289px;width:226px;height:37px">Email Address</div>
  <div class="abs field" style="left:81px;top:348px;width:226px;height:37px">Phone Number</div>
  <div class="abs field" style="left:324px;top:232px;width:228px;height:96px">Message</div>
  <div class="abs submit" style="left:324px;top:348px;width:228px;height:37px">SUBMIT</div>

  <div class="abs vsep" style="left:604px;top:168px;height:240px"></div>
  <svg class="abs" style="left:626px;top:169px" width="16" height="22"><rect x="1" y="4" width="14" height="17" fill="none" stroke="#fff" stroke-width="2"/><rect x="4" y="1" width="8" height="5" fill="#fff"/></svg>
  <div class="abs f-title" style="left:650px;top:169px">Quick Links</div>
  <ul class="abs links">
    <li class="current">Home</li><li>About</li><li>Services</li><li>Blog</li><li>Videos</li><li>Programs</li><li>Contact</li>
  </ul>

  <div class="abs vsep" style="left:839px;top:168px;height:240px"></div>
  <svg class="abs" style="left:869px;top:170px" width="22" height="20"><rect x="1" y="3" width="20" height="14" fill="none" stroke="#fff" stroke-width="2"/><path d="M1 3l10 8 10-8" stroke="#fff" stroke-width="2" fill="none"/></svg>
  <div class="abs f-title" style="left:898px;top:169px">Contact Information</div>
  <svg class="abs" style="left:869px;top:226px" width="14" height="20"><path d="M7 19C3 13 1 10 1 7a6 6 0 0112 0c0 3-2 6-6 12z" fill="#ccc"/><circle cx="7" cy="7" r="2.2" fill="#1b1b1b"/></svg>
  <p class="abs c-text" style="left:896px;top:223px">VORANEL<br>Lorem ipsum dolor sit amet, consec<br>tetuer adipiscing elit, sed</p>
  <svg class="abs" style="left:868px;top:308px" width="16" height="16"><path d="M4 1l3 3-2 2c1 2 3 4 5 5l2-2 3 3-2 3C7 15 1 9 1 3z" fill="#ccc"/></svg>
  <div class="abs c-text" style="left:896px;top:305px;font-size:14px;color:var(--white)">123-456-7890</div>
  <svg class="abs" style="left:868px;top:356px" width="16" height="12"><rect x="1" y="1" width="14" height="10" fill="none" stroke="#ccc" stroke-width="1.5"/><path d="M1 1l7 5 7-5" stroke="#ccc" stroke-width="1.5" fill="none"/></svg>
  <div class="abs c-text" style="left:896px;top:351px">info@voranel.com</div>
</footer>

<div class="abs to-top"></div>
<div class="abs copyright" style="left:0;width:1200px">COPYRIGHT 2016 VORANEL | ALL RIGHT RESERVED.</div>

</body>
</html>
```